Australian Software Consultancy needs new Business Card Design

Design Business Card based on existing design artefacts (attached). We are open to all designs. As its a 2 sided design and we thought it might be quite striking to have one side with a black background and te other side with a white background.

Target Market(s)

Financial Services mainly.

Industry/Entity Type

Business

Contact Information for Business Card

Name :
Position :
Email :

Requirements
Must have
• Funky design using our existing assets

```html
<!DOCTYPE html>
<html lang="en">
<head>
<meta charset="utf-8">
<title>Clearfield Labs – Business Card</title>
<link href="https://fonts.googleapis.com/css2?family=Montserrat:wght@400;500;700&display=swap" rel="stylesheet">
<style>
  :root {
    --ink: #0d0d0d;
    --paper: #ffffff;
    --accent: #e3202a;
    --backdrop: #9a9a9a;
    --muted: #2b2b2b;
  }
  html, body {
    margin: 0;
    padding: 0;
    width: 1200px;
    height: 945px;
    overflow: hidden;
    background: var(--backdrop);
    font-family: "Montserrat", sans-serif;
  }
  .canvas {
    position: relative;
    width: 1200px;
    height: 945px;
  }
  .card {
    position: absolute;
    left: 280px;
    width: 640px;
    height: 365px;
    border-radius: 14px;
    overflow: hidden;
    box-shadow: 0 14px 30px rgba(0,0,0,0.35);
  }
  .card--front { top: 88px; }
  .card--back { top: 492px; }
  .card svg { display: block; }
  .wordmark {
    font-family: "Montserrat", sans-serif;
    font-weight: 700;
    font-size: 50px;
    letter-spacing: 2px;
    fill: var(--paper);
  }
  .brand-name {
    font-family: "Montserrat", sans-serif;
    font-weight: 700;
    font-size: 26px;
    fill: var(--accent);
  }
  .person-name {
    font-weight: 700;
    font-size: 24px;
    fill: var(--accent);
  }
  .person-role {
    font-weight: 500;
    font-size: 12px;
    letter-spacing: 3px;
    fill: var(--muted);
  }
  .contact-line {
    font-weight: 500;
    font-size: 12px;
    letter-spacing: 0.6px;
    fill: var(--muted);
  }
</style>
</head>
<body>
<div class="canvas">

  <!-- Front side -->
  <div class="card card--front">
    <svg width="640" height="365" viewBox="0 0 640 365">
      <rect class="front-ground" width="640" height="365" fill="var(--ink)"/>
      <text class="wordmark" x="320" y="200" text-anchor="middle">CLEARFIELD LABS</text>
      <polygon class="front-tab" points="340,365 352,342 640,330 640,365" fill="var(--paper)"/>
      <rect class="front-rule" x="0" y="358" width="345" height="7" fill="var(--accent)"/>
    </svg>
  </div>

  <!-- Back side -->
  <div class="card card--back">
    <svg width="640" height="365" viewBox="0 0 640 365">
      <rect class="back-ground" width="640" height="365" fill="var(--ink)"/>
      <polygon class="info-band" points="0,214 110,214 124,204 548,204 592,160 640,160 640,318 0,318" fill="var(--paper)"/>
      <polyline class="info-band-edge" points="75,210 108,210 122,199 545,199 586,162" fill="none" stroke="var(--accent)" stroke-width="4" stroke-linejoin="miter"/>
      <rect class="footer-rule" x="0" y="326" width="640" height="3" fill="var(--accent)"/>

      <g class="brand-lockup">
        <circle cx="215" cy="106" r="16" fill="none" stroke="var(--accent)" stroke-width="4"/>
        <text class="brand-name" x="242" y="115">Clearfield Labs</text>
      </g>

      <g class="identity">
        <text class="person-name" x="300" y="262" text-anchor="end">Martin R. Hale</text>
        <text class="person-role" x="300" y="284" text-anchor="end">FOUNDER / CEO</text>
      </g>

      <line class="divider" x1="320" y1="230" x2="320" y2="292" stroke="var(--ink)" stroke-width="2"/>

      <g class="contacts">
        <g class="contact contact--phone">
          <rect x="338" y="232" width="12" height="12" rx="3" fill="var(--accent)"/>
          <path d="M341.5 235 q0 4 4.5 6.5 l1.2-1.4 -1.6-1 -0.8 0.8 q-1.5-0.8-2.2-2.2 l0.8-0.8 -1-1.6z" fill="var(--paper)"/>
          <text class="contact-line" x="360" y="242">555.010.284</text>
        </g>
        <g class="contact contact--email">
          <rect x="338" y="253" width="12" height="12" rx="3" fill="var(--accent)"/>
          <path d="M341 256.5 h6 v5 h-6z M341 256.5 l3 2.6 3-2.6" fill="none" stroke="var(--paper)" stroke-width="1"/>
          <text class="contact-line" x="360" y="263">hello@clearfield-labs.com</text>
        </g>
        <g class="contact contact--web">
          <rect x="338" y="274" width="12" height="12" rx="3" fill="var(--accent)"/>
          <circle cx="344" cy="280" r="3.3" fill="none" stroke="var(--paper)" stroke-width="1"/>
          <line x1="340.7" y1="280" x2="347.3" y2="280" stroke="var(--paper)" stroke-width="1"/>
          <text class="contact-line" x="360" y="284">www.clearfield-labs.com</text>
        </g>
      </g>
    </svg>
  </div>

</div>
</body>
</html>
```